Juno's Bakes Tartlets LLC website

Artisan cheesecake business looking for excellent talent to design bright, fun, engaging website for our company. We also recently acquired a food truck so we are able to cater and attend food truck events.
Our mission is to create fun, unique, delicious flavors of cheesecake and we bake them in mason jars and whole cheesecakes. We strive to exceed our customers' expectations in everything we do.
Updates
Target Market(s)
Foodies, cheesecake lovers, dessert lovers, food truck people,
Industry/Entity Type
Dessert, Catering, Pop Up events, Food truck
Coding
Coded - Design and coding required
Number of Pages Required
4 page
Requirements
Must have
- Pictures of my cheesecakes
Nice to have
- Bright, colorful, eye-catching design with a good flow

```html
<!DOCTYPE html>
<html lang="en">
<head>
<meta charset="utf-8">
<title>Juno's Bakes Tartlets</title>
<link rel="stylesheet" href="https://fonts.googleapis.com/css2?family=Caveat:wght@400;500&family=Lato:wght@400;700;900&display=swap">
<style>
:root{
  --pink:#f7b3c2;
  --pink-soft:#fbc6d1;
  --pink-text:#f39bb0;
  --ink:#222;
  --body:#444;
  --grey-bg:#f4f4f4;
  --black:#000;
  --white:#fff;
  --hero-dark:#3b2a22;
  --hero-light:#b59a8a;
}
*{margin:0;padding:0;box-sizing:border-box}
html,body{width:1200px;height:3791px;overflow:hidden}
body{position:relative;background:var(--white);font-family:'Lato',sans-serif;color:var(--body)}
.abs{position:absolute}
.script{font-family:'Caveat',cursive;font-weight:400;color:var(--ink)}

/* header */
.site-header{left:0;top:0;width:1200px;height:70px;background:var(--white);z-index:5}
.brand-badge{left:126px;top:-4px;width:126px;height:126px;border-radius:50%;background:var(--pink);border:6px solid var(--white);box-shadow:0 2px 6px rgba(0,0,0,.15);display:flex;align-items:center;justify-content:center;z-index:6}
.brand-badge span{font-family:'Lato',sans-serif;font-weight:700;color:var(--white);font-size:15px}
.main-nav a{position:absolute;top:29px;font-size:13px;font-weight:700;color:var(--ink);text-decoration:none;letter-spacing:.2px}
.main-nav a.active{color:var(--pink-text);font-weight:400}
.btn{display:flex;align-items:center;justify-content:center;background:var(--pink);color:var(--white);font-weight:900;font-size:15px;border-radius:22px;letter-spacing:.3px}

/* hero */
.hero{left:0;top:70px;width:1200px;height:660px;background:radial-gradient(ellipse at 50% 40%,var(--hero-light),var(--hero-dark) 85%)}
.hero-welcome{left:0;top:248px;width:1200px;text-align:center;color:var(--white);font-size:30px;letter-spacing:9px;font-weight:400}
.hero-title{left:0;top:268px;width:1200px;text-align:center;color:var(--white);font-size:128px;line-height:1}
.hero-copy{left:180px;top:422px;width:840px;text-align:center;color:var(--white);font-size:14px;line-height:27px}
.hero-dots i{position:absolute;left:1120px;width:10px;height:10px;border-radius:50%;background:var(--white)}
.hero-dots i.on{background:var(--pink)}

/* about */
.about-photo{left:127px;top:806px;width:426px;height:426px;border-radius:50%;border:5px solid var(--pink);padding:10px;background:var(--white)}
.about-photo div{width:100%;height:100%;border-radius:50%;background:linear-gradient(150deg,#7a6a5a,#3a3b3e 60%,#c9a0a8)}
.section-title{font-size:56px;line-height:1}
.rule{height:4px;width:52px;background:var(--pink)}
.about-copy{left:602px;top:866px;width:455px;font-size:13.5px;line-height:28px;text-align:justify;color:var(--body)}

/* menu */
.menu{left:0;top:1347px;width:1200px;height:658px;background:var(--grey-bg)}
.card{width:298px;height:352px;background:var(--white);border-radius:16px;box-shadow:0 2px 8px rgba(0,0,0,.08);padding:6px}
.card .photo{height:260px;border-radius:12px}
.card h3{margin-top:14px;text-align:center;font-family:'Caveat',cursive;font-weight:500;font-size:30px;color:var(--ink);line-height:1}
.card p{text-align:center;font-size:13px;color:var(--pink-text);margin-top:6px}
.card.featured{background:var(--pink)}
.card.featured h3{font-family:'Lato',sans-serif;font-weight:400;font-size:20px;color:var(--white);margin-top:16px}
.card.featured p{color:var(--white)}

/* testimonials */
.testimonials{left:0;top:2005px;width:590px;height:546px;background:var(--pink)}
.testimonial-photo{left:590px;top:2005px;width:610px;height:546px;background:linear-gradient(180deg,#6f8a55,#8d8f8b 45%,#6a6a6c)}
.quote{left:28px;top:2176px;width:534px;text-align:center;color:var(--white);font-style:italic;font-size:16px;line-height:35.3px}

/* gallery */
.tile{border-radius:14px}

/* footer */
.footer-logo{left:162px;top:3461px;width:174px;height:174px;border-radius:50%;background:var(--pink);display:flex;align-items:center;justify-content:center}
.footer-logo span{color:var(--white);font-weight:700;font-size:18px}
.footer-col h4{position:absolute;color:var(--white);font-size:15px;font-weight:700}
.footer-col li{position:absolute;list-style:none;color:var(--white);font-size:13.5px}
.footer-col li::before{content:"»";margin-right:16px;font-weight:700}
.contact-line{color:var(--white);font-size:13.5px;line-height:28px}
.icon-dot{width:28px;height:28px;border-radius:50%;background:var(--pink);display:flex;align-items:center;justify-content:center}
.social i{position:absolute;top:3740px;width:29px;height:29px;border-radius:50%;background:var(--pink)}
</style>
</head>
<body>

<header class="abs site-header">
  <nav class="main-nav">
    <a class="active" style="left:351px">HOME</a>
    <a style="left:422px">ABOUT US</a>
    <a style="left:517px">OUR MENU</a>
    <a style="left:618px">BLOGS</a>
    <a style="left:691px">GALLERY</a>
    <a style="left:778px">CONTACT US</a>
  </nav>
  <div class="abs btn" style="left:926px;top:16px;width:141px;height:41px">LOGIN</div>
</header>
<div class="abs brand-badge"><span>Juno's Bakes</span></div>

<section>
  <div class="abs hero" role="img" aria-label="Close-up photo of a cheesecake topped with piped frosting and chocolate cups"></div>
  <div class="abs hero-welcome">WELCOME TO</div>
  <h1 class="abs hero-title script" style="color:#fff">Juno's Bakes</h1>
  <p class="abs hero-copy">Lorem ipsum dolor sit amet, consectetur adipiscing elit, sed do eiusmod tempor incididunt ut labore et dolore magna aliqua. Quis ipsum suspendisse ultrices gravida. Risus commodo viverra maecenas accumsan lacus vel facilisis.</p>
  <div class="abs btn" style="left:521px;top:486px;width:156px;height:38px">GET STARTED</div>
  <div class="hero-dots"><i style="top:351px"></i><i class="on" style="top:373px"></i><i style="top:395px"></i><i style="top:417px"></i></div>
  <svg class="abs" style="left:0;top:600px" width="1200" height="140" viewBox="0 600 1200 140">
    <path d="M0 718 C80 680 150 630 240 635 C360 640 450 725 590 724 C730 723 860 630 1000 630 C1100 630 1160 665 1200 690 L1200 740 L0 740Z" fill="#fff"/>
    <path d="M0 718 C80 680 150 630 240 635 C360 640 450 725 590 724 C730 723 860 630 1000 630 C1100 630 1160 665 1200 690" fill="none" stroke="#f7b3c2" stroke-width="7"/>
  </svg>
</section>

<section>
  <div class="abs about-photo"><div role="img" aria-label="Photo of the baker smiling behind the counter"></div></div>
  <h2 class="abs section-title script" style="left:602px;top:776px">About Juno's Bakes</h2>
  <div class="abs rule" style="left:602px;top:838px"></div>
  <p class="abs about-copy">Lorem ipsum dolor sit amet, consectetur adipiscing elit, sed do eiusmod tempor incididunt ut labore et dolore magna aliqua. Quis ipsum suspendisse ultrices gravida. Risus commodo viverra maecenas accumsan lacus vel facilisis. orem ipsum dolor sit amet, consectetur adipiscing elit, sed do eiusmod tempor incididunt ut labore et dolore magna aliqua. Ut enim ad minim veniam, quis nostrud exercitation ullamco laboris nisi ut aliquip ex ea commodo consequat. Duis aute irure dolor in reprehenderit in voluptate velit esse cillum dolore eu fugiat nulla pariatur. Excepteur sint occaecat cupidatat non proident, sunt in culpa qui officia deserunt mollit anim id est laborum.omnis iste natus error sit voluptatem accusantium doloremque laudantium, totam rem aperiam, eaque ipsa quae ab illo inventore veritatis et quasi architecto beatae vitae dicta sunt explicabo.</p>
  <div class="abs btn" style="left:602px;top:1218px;width:158px;height:41px">GET STARTED</div>
</section>

<section>
  <div class="abs menu"></div>
  <h2 class="abs section-title script" style="left:0;width:1200px;text-align:center;top:1418px">Our Menu</h2>
  <div class="abs rule" style="left:574px;top:1478px"></div>
  <svg class="abs" style="left:76px;top:1680px" width="24" height="34"><path d="M18 3 L5 17 L18 31" fill="none" stroke="#222" stroke-width="2.5"/></svg>
  <svg class="abs" style="left:1100px;top:1680px" width="24" height="34"><path d="M6 3 L19 17 L6 31" fill="none" stroke="#222" stroke-width="2.5"/></svg>
  <div class="abs card" style="left:132px;top:1531px">
    <div class="photo" role="img" aria-label="Photo of a banana cheesecake slice" style="background:linear-gradient(180deg,#e9d3b0,#c99c62 60%,#eeeeee)"></div>
    <h3>Lorem ipsum dolor sit</h3><p>Price : $ 120.00</p>
  </div>
  <div class="abs card featured" style="left:451px;top:1531px">
    <div class="photo" role="img" aria-label="Photo of a chocolate cookies and cream cheesecake slice" style="background:linear-gradient(180deg,#cfd3d6,#3a2a22 40%,#c9c3b5 70%,#2a221f)"></div>
    <h3>Lorem ipsum dolor sit</h3><p>Price : $ 120.00</p>
  </div>
  <div class="abs card" style="left:770px;top:1531px">
    <div class="photo" role="img" aria-label="Photo of a spiced cake cheesecake slice" style="background:linear-gradient(180deg,#b9b7b2,#c2a08a 50%,#f3eee2 80%,#ddd)"></div>
    <h3>Lorem ipsum dolor sit</h3><p>Price : $ 120.00</p>
  </div>
</section>

<section>
  <div class="abs testimonials"></div>
  <h2 class="abs section-title script" style="left:0;width:590px;text-align:center;top:2074px;color:#fff">Our Client Testimonials</h2>
  <div class="abs" style="left:266px;top:2138px;width:52px;height:4px;background:#fff"></div>
  <p class="abs quote">"Lorem ipsum dolor sit amet, consectetur adipiscing elit, sed do eiusmod tempor incididunt ut labore et dolore magna aliqua. Ut enim ad minim veniam, quis nostrud exercitation ullamco laboris nisi ut aliquip ex ea commodo consequat. Duis aute irure dolor in reprehenderit in voluptate velit esse cillum dolore eu fugiat nulla pariatur. Excepteur sint occaecat cupidatat non proident sunt in culpa qui officia"</p>
  <div class="abs script" style="left:0;width:570px;text-align:center;top:2396px;font-size:24px;color:#fff">Mara Ellison</div>
  <svg class="abs" style="left:257px;top:2456px" width="56" height="10"><circle cx="5" cy="5" r="5" fill="#fff"/><circle cx="19" cy="5" r="5" fill="#fbd3dc"/><circle cx="33" cy="5" r="5" fill="#fbd3dc"/><circle cx="47" cy="5" r="5" fill="#fbd3dc"/></svg>
  <div class="abs testimonial-photo" role="img" aria-label="Photo of two happy customers standing beside the food truck"></div>
</section>

<section>
  <h2 class="abs section-title script" style="left:0;width:1200px;text-align:center;top:2670px">Our Gallery</h2>
  <div class="abs rule" style="left:574px;top:2733px"></div>
  <div class="abs tile" style="left:135px;top:2788px;width:460px;height:437px;background:linear-gradient(180deg,#e8a9b8,#f0b7c4 70%,#555)" role="img" aria-label="Photo of the pink dessert food truck"></div>
  <div class="abs tile" style="left:604px;top:2788px;width:225px;height:212px;background:linear-gradient(180deg,#f2c6cf,#b98c6e)" role="img" aria-label="Photo of cheesecakes baked in mason jars"></div>
  <div class="abs tile" style="left:838px;top:2788px;width:225px;height:212px;background:linear-gradient(160deg,#ddd,#d9a766 50%,#6a4a2e)" role="img" aria-label="Photo of a caramel cheesecake slice with ice cream"></div>
  <div class="abs tile" style="left:604px;top:3012px;width:225px;height:213px;background:linear-gradient(180deg,#eee,#e9dfd0 50%,#8a5a30)" role="img" aria-label="Photo of a decorated celebration cheesecake"></div>
  <div class="abs tile" style="left:838px;top:3012px;width:225px;height:213px;background:linear-gradient(180deg,#4f7a3a,#b52a34 50%,#f2efe8)" role="img" aria-label="Photo of a red velvet cheesecake slice"></div>
</section>

<footer>
  <svg class="abs" style="left:0;top:3280px" width="1200" height="511" viewBox="0 3280 1200 511">
    <path d="M0 3300 C120 3360 250 3400 420 3398 C600 3396 700 3320 860 3318 C1000 3316 1120 3330 1200 3290 L1200 3791 L0 3791Z" fill="#000"/>
    <path d="M0 3300 C120 3360 250 3400 420 3398 C600 3396 700 3320 860 3318 C1000 3316 1120 3330 1200 3290" fill="none" stroke="#f7b3c2" stroke-width="7"/>
  </svg>
  <div class="abs footer-logo"><span>Juno's Bakes</span></div>
  <div class="footer-col">
    <h4 style="left:422px;top:3458px">QUICK LINKS</h4>
    <ul>
      <li style="left:418px;top:3494px">Home</li>
      <li style="left:418px;top:3522px">About Us</li>
      <li style="left:418px;top:3550px">Our Menu</li>
      <li style="left:418px;top:3578px">Blogs</li>
      <li style="left:418px;top:3606px">Gallery</li>
    </ul>
    <h4 style="left:599px;top:3458px">LEGAL</h4>
    <ul>
      <li style="left:595px;top:3494px">Privacy Policy</li>
      <li style="left:595px;top:3522px">Terms &amp; Conditions</li>
      <li style="left:595px;top:3550px">Contact Us</li>
      <li style="left:595px;top:3578px">FAQ</li>
    </ul>
    <h4 style="left:807px;top:3458px">CONTACT US</h4>
  </div>
  <div class="abs icon-dot" style="left:807px;top:3491px"><svg width="14" height="16"><path d="M7 1 C3.5 1 1.5 3.5 1.5 6 C1.5 9.5 7 15 7 15 C7 15 12.5 9.5 12.5 6 C12.5 3.5 10.5 1 7 1Z" fill="#fff"/><circle cx="7" cy="6" r="2" fill="#f7b3c2"/></svg></div>
  <p class="abs contact-line" style="left:851px;top:3490px;width:220px">123 Lorem ipsum dolor sit amet consectetur adipiscing elit.</p>
  <div class="abs icon-dot" style="left:807px;top:3564px"><svg width="14" height="14"><path d="M3 1 L5.5 1 L6.5 4 L5 5.5 C6 7.5 7 8.5 8.5 9 L10 7.5 L13 8.5 L13 11 C13 12 12 13 11 13 C5.5 12.5 1.5 8.5 1 3 C1 2 2 1 3 1Z" fill="#fff"/></svg></div>
  <p class="abs contact-line" style="left:851px;top:3564px">+1 888 888 8888</p>
  <div class="abs icon-dot" style="left:807px;top:3619px"><svg width="14" height="12"><rect x="1" y="2" width="12" height="9" rx="1" fill="#fff"/><path d="M1 3 L7 7 L13 3" fill="none" stroke="#f7b3c2" stroke-width="1.3"/></svg></div>
  <p class="abs contact-line" style="left:851px;top:3619px">hello@junosbakes.com</p>
  <div class="abs" style="left:84px;top:3686px;width:1032px;height:1px;background:#666"></div>
  <p class="abs" style="left:0;width:1200px;text-align:center;top:3705px;color:#fff;font-size:13.5px">© Copyrights 2022 Juno's Bakes | &nbsp; All Rights Reserved</p>
  <div class="social"><i style="left:520px"></i><i style="left:564px"></i><i style="left:608px"></i><i style="left:652px"></i></div>
</footer>

</body>
</html>
```